Home page makeover

Take my existing home page, www.maplecrestharborline.com and redesign layout to look more current considering today's touch design prevalence.
Reuse existing elements or suggest improved ones if available.
I generally have average CSS and HTML skills using div containers, defining lists and using columns to create the code to support the layout.
Updates
Just wanted to send out a quick message to thank all of you for your submissions. Many of you offered nice designs, but unfortunately could only choose one.
Target Market(s)
Generally targeting individuals with some assets for retirement. Basically your average working professional or business owner.
Industry/Entity Type
It Support
Look and feel
Each slider illustrates characteristics of the customer's brand and the style your logo design should communicate.

```html
<!DOCTYPE html>
<html lang="en">
<head>
<meta charset="utf-8">
<title>Maplecrest Harborline – Home</title>
<link href="https://fonts.googleapis.com/css2?family=Oswald:wght@400;500;600;700&family=Open+Sans:wght@400;600;700&display=swap" rel="stylesheet">
<style>
:root{
  --green:#6fae1e;
  --green-dark:#175e2a;
  --green-deep:#0f4a20;
  --blue:#1f5fa8;
  --blue-dark:#184b86;
  --red:#d8262b;
  --ink:#2e2e2e;
  --muted:#6b6b6b;
  --line:#d4d9dd;
  --page:#eef1f3;
  --white:#ffffff;
}
*{box-sizing:border-box;margin:0;padding:0}
html,body{width:798px;height:1200px;overflow:hidden}
body{position:relative;background:var(--page);font-family:"Open Sans",Arial,sans-serif;color:var(--ink)}
.site-header{position:absolute;left:0;top:0;width:798px;height:72px;background:var(--white);z-index:3}
.brand{position:absolute;left:92px;top:10px;display:flex;align-items:center;gap:8px}
.brand-mark{width:22px;height:22px;background:var(--green)}
.brand-name{font-family:"Oswald",sans-serif;font-weight:600;font-size:20px;color:var(--green-dark);line-height:1}
.brand-tag{font-size:9px;color:var(--green-dark);letter-spacing:.5px;margin-top:3px}
.main-nav{position:absolute;right:92px;top:24px;display:flex;align-items:center;gap:14px;font-family:"Oswald",sans-serif;font-size:14px;font-weight:500;color:#333}
.btn-outline{border:2px solid var(--green);padding:3px 10px;font-size:13px;color:var(--green-dark)}
.hero{position:absolute;left:0;top:72px;width:798px;height:320px;background:linear-gradient(180deg,#cfe4f1 0%,#e9f1f3 55%,#d9cfb9 100%)}
.steps{position:absolute;left:0;top:222px;width:798px;height:150px;z-index:2}
.step{position:absolute;top:0;width:150px;height:150px}
.step-photo{width:150px;height:150px;border-radius:50%;border:5px solid var(--white);box-shadow:0 2px 6px rgba(0,0,0,.25)}
.step-label{position:absolute;left:18px;bottom:-6px;width:114px;height:28px;color:var(--white);font-family:"Oswald",sans-serif;font-weight:600;font-size:15px;letter-spacing:1px;text-align:center;line-height:28px}
.content{position:absolute;left:92px;top:392px;width:614px;height:596px;background:var(--white)}
.features{position:absolute;left:0;top:0;width:285px;height:596px;background:#f6f8f9}
.section-title{font-family:"Oswald",sans-serif;font-weight:600;font-size:22px;color:var(--blue);letter-spacing:.5px}
.features .section-title{position:absolute;left:14px;top:10px}
.feature-list{position:absolute;left:14px;top:48px;width:262px;list-style:none}
.feature-list li{position:relative;padding-left:22px;margin-bottom:7px;font-size:9.4px;line-height:12.5px;color:#444}
.feature-list svg{position:absolute;left:0;top:1px}
.beach-photo{position:absolute;left:0;top:314px;width:285px;height:216px;background:linear-gradient(180deg,#a9d1ee 0%,#cbe3f1 45%,#e4d6b8 80%,#d6c39c 100%)}
.signup-bar{position:absolute;left:0;top:530px;width:285px;height:66px;display:flex}
.signup-cta{width:77px;background:var(--green);color:var(--white);font-family:"Oswald",sans-serif;font-size:21px;font-weight:600;display:flex;align-items:center;justify-content:center}
.price{width:104px;background:var(--blue);color:var(--white);font-family:"Oswald",sans-serif;padding:9px 7px;border-left:1px solid rgba(255,255,255,.35)}
.price strong{display:block;font-size:17px;font-weight:600;line-height:20px;white-space:nowrap}
.price span{display:block;font-size:9.5px;line-height:11px;margin-top:2px}
.price.alt{background:var(--blue-dark)}
.sidebar{position:absolute;left:306px;top:14px;width:306px}
.video{position:relative;width:306px;height:138px;background:linear-gradient(160deg,#3a3a3a,#111);border:3px solid #ccc}
.video-play{position:absolute;left:128px;top:46px;width:44px;height:32px;border-radius:6px;background:rgba(0,0,0,.7);border:1px solid #888}
.video-bar{position:absolute;left:0;bottom:0;width:100%;height:14px;background:#222}
.sidebar .section-title{margin-top:22px;margin-left:4px}
.testimonial{position:relative;width:296px;height:78px;margin:12px 0 0 4px;background:var(--white);border:1px solid var(--line);padding:10px 44px 0 10px}
.testimonial p{font-size:10px;line-height:13px;color:#555}
.testimonial cite{display:block;font-style:normal;font-weight:700;font-size:9.5px;color:#333;margin-top:4px}
.testimonial svg{position:absolute;right:8px;top:-8px}
.site-footer{position:absolute;left:0;top:1004px;width:798px;height:196px;background:var(--green-dark)}
.footer-brand{position:absolute;left:130px;top:44px;display:flex;align-items:center;gap:8px;color:var(--white)}
.footer-brand .brand-mark{background:var(--white)}
.footer-brand .brand-name{color:var(--white);font-size:22px}
.footer-brand .brand-tag{color:var(--white)}
.keep{position:absolute;left:320px;top:24px;color:var(--white)}
.keep h3{font-family:"Oswald",sans-serif;font-weight:500;font-size:19px}
.keep .email{font-size:10.5px;margin-top:6px}
.newsletter{display:flex;margin-top:8px}
.newsletter .field{width:150px;height:20px;background:var(--white);font-size:9px;color:#888;padding:4px 6px}
.newsletter .submit{height:20px;background:var(--green);color:var(--white);font-size:9px;font-weight:700;padding:4px 8px}
.social{display:flex;gap:6px;margin-top:8px}
.social span{width:22px;height:22px;border-radius:50%;background:var(--white)}
.copyright{position:absolute;left:0;bottom:0;width:798px;height:30px;background:var(--green-deep);color:var(--green);font-size:8.5px;letter-spacing:.6px;text-align:center;line-height:30px}
</style>
</head>
<body>
<header class="site-header">
  <div class="brand">
    <span class="brand-mark"></span>
    <div><div class="brand-name">MHL</div><div class="brand-tag">Maplecrest Harborline</div></div>
  </div>
  <nav class="main-nav">
    <span>HOME</span><span>ABOUT</span><span>CONTACT</span>
    <span class="btn-outline">SIGN IN</span><span class="btn-outline">SIGN UP</span>
  </nav>
</header>

<section class="hero" role="img" aria-label="Smiling retired couple with bicycles on a sunny beach"></section>

<div class="steps">
  <div class="step" style="left:90px">
    <div class="step-photo" role="img" aria-label="Hand holding a magnifying glass over documents" style="background:linear-gradient(135deg,#f2f2f2,#b9c3c9)"></div>
    <div class="step-label" style="background:var(--red)">IDENTIFY</div>
  </div>
  <div class="step" style="left:245px">
    <div class="step-photo" role="img" aria-label="Pen resting on financial charts" style="background:linear-gradient(135deg,#eef3f6,#a8bccb)"></div>
    <div class="step-label" style="background:var(--green)">PLAN</div>
  </div>
  <div class="step" style="left:400px">
    <div class="step-photo" role="img" aria-label="Wooden beach chairs by the sea" style="background:linear-gradient(180deg,#8cc3e6,#e8d5b0)"></div>
    <div class="step-label" style="background:var(--red)">RETIRE</div>
  </div>
</div>

<main class="content">
  <section class="features">
    <h2 class="section-title">FEATURES</h2>
    <ul class="feature-list">
      <li><svg width="14" height="12" viewBox="0 0 14 12"><path d="M1 6l4 4 8-9" fill="none" stroke="#6fae1e" stroke-width="2.5"/></svg>Identify and project your retirement needs and expectations including basic living expenses, housing costs, recreation, big ticket non-recurring items, medical and nursing home care.</li>
      <li><svg width="14" height="12" viewBox="0 0 14 12"><path d="M1 6l4 4 8-9" fill="none" stroke="#6fae1e" stroke-width="2.5"/></svg>Identify and project all sources of retirement income including retirement savings, other savings, pension plans, Social Security, life insurance and working part-time during retirement for a period of time.</li>
      <li><svg width="14" height="12" viewBox="0 0 14 12"><path d="M1 6l4 4 8-9" fill="none" stroke="#6fae1e" stroke-width="2.5"/></svg>Strategize tapping into the equity of your real estate including swapping your primary residence for a different home or retirement area, or selling and renting.</li>
      <li><svg width="14" height="12" viewBox="0 0 14 12"><path d="M1 6l4 4 8-9" fill="none" stroke="#6fae1e" stroke-width="2.5"/></svg>Produce easy to understand results featuring the Retirement Readiness Gauge.</li>
      <li><svg width="14" height="12" viewBox="0 0 14 12"><path d="M1 6l4 4 8-9" fill="none" stroke="#6fae1e" stroke-width="2.5"/></svg>Save multiple plans, track returns, revisit and edit your retirement plan.</li>
    </ul>
    <div class="beach-photo" role="img" aria-label="Retired couple sitting together on a beach facing the sea"></div>
    <div class="signup-bar">
      <div class="signup-cta">SIGN UP</div>
      <div class="price"><strong>ONLY $19.99</strong><span>FOR A ONE YEAR MEMBERSHIP</span></div>
      <div class="price alt"><strong>ONLY $9.99</strong><span>PER YEAR AFTER THAT</span></div>
    </div>
  </section>

  <aside class="sidebar">
    <div class="video" role="img" aria-label="Introductory video about retirement planning">
      <div class="video-play"><svg width="44" height="32" viewBox="0 0 44 32"><path d="M18 10l10 6-10 6z" fill="#fff"/></svg></div>
      <div class="video-bar"></div>
    </div>
    <h2 class="section-title">TESTIMONIAL</h2>
    <div class="testimonial"><p>"This site is a great place to get a handle on your retirement strategy"</p><cite>Dana, Ohio</cite><svg width="26" height="26" viewBox="0 0 26 26"><path d="M4 22l2-7L18 3l5 5-12 12z" fill="#8ed0e8" stroke="#3a9cc2"/></svg></div>
    <div class="testimonial"><p>"This is the best retirement projection tool for the average user that puts it all together"</p><cite>Mark, Oregon</cite><svg width="26" height="26" viewBox="0 0 26 26"><path d="M4 22l2-7L18 3l5 5-12 12z" fill="#8ed0e8" stroke="#3a9cc2"/></svg></div>
    <div class="testimonial"><p>"This site is a great place to get a handle on your retirement strategy"</p><cite>Dana, Ohio</cite><svg width="26" height="26" viewBox="0 0 26 26"><path d="M4 22l2-7L18 3l5 5-12 12z" fill="#8ed0e8" stroke="#3a9cc2"/></svg></div>
    <div class="testimonial"><p>"This is the best retirement projection tool for the average user that puts it all together"</p><cite>Mark, Oregon</cite><svg width="26" height="26" viewBox="0 0 26 26"><path d="M4 22l2-7L18 3l5 5-12 12z" fill="#8ed0e8" stroke="#3a9cc2"/></svg></div>
  </aside>
</main>

<footer class="site-footer">
  <div class="footer-brand">
    <span class="brand-mark"></span>
    <div><div class="brand-name">MHL</div><div class="brand-tag">Maplecrest Harborline</div></div>
  </div>
  <div class="keep">
    <h3>Keep in touch.</h3>
    <div class="email">contact@maplecrestharborline.com</div>
    <div class="newsletter"><span class="field">Enter your email</span><span class="submit">SUBMIT</span></div>
    <div class="social"><span></span><span></span></div>
  </div>
  <div class="copyright">© 2013 COPYRIGHT MAPLECREST HARBORLINE, INC. ALL RIGHTS RESERVED.</div>
</footer>
</body>
</html>
```